Coffee House With Cycling Theme Wants Business Cards

We want to create a business card for a coffee house that has a cycling theme. We expect to use the current logo on one side of the business card and we have been considering adding the words 'COFFEE HOUSE' underneath (see example). For the other side of the business card we want an interesting design with tag-line, address and social media links (the normal business card stuff). See examples provided but we are not fixed on having it exactly as shown, we are very open to great creative ideas. Please note our logo has the initials ‘RM' in orange embedded in the design and this must be retained. However, you can play with the words COFFEE HOUSE as well as use the orange color on the backside of the business card, as you see fit. For an image on the backside of the business card it can be a photo, hand-drawn or whatever but it must visually combine coffee and cycling in some way. The interior of the Coffee House will be reclaimed wood, rustic and have an urban feel to it with cycling artifacts hanging from the walls/ceiling, etc. Finally, it would be beneficial if the business card design elements can be easily used on flyers and other promotional assets. Good luck, we are looking forward to seeing your creative ideas.

Target Market(s)

Coffee lovers and cycling fans

Contact Information for Business Card

See project description.

Colors

Designer to choose colors to be used in the design.

Requirements
Must have
• Must use the current logo provided and combine a coffee and bike theme.
Nice to have
• Orange is used in current logo and could be used as an accent color on the backside of the business card.

```html
<!DOCTYPE html>
<html lang="en">
<head>
<meta charset="utf-8">
<title>RM Coffee House – Business Cards</title>
<link rel="stylesheet" href="https://fonts.googleapis.com/css2?family=Open+Sans:wght@300;400;600;700&display=swap">
<style>
  :root {
    --stage: #e4e4e6;
    --orange: #f4621c;
    --ink: #1b1b1b;
    --graphite: #3a3a3a;
    --white: #ffffff;
    --wood-light: #c49a66;
    --wood-dark: #7d5530;
    --cup: #eef0f2;
  }
  * { box-sizing: border-box; margin: 0; padding: 0; }
  html, body { width: 1200px; height: 800px; overflow: hidden; }
  body {
    background: var(--stage);
    font-family: "Open Sans", Arial, sans-serif;
    position: relative;
  }
  .card {
    position: absolute;
    top: 245px;
    width: 540px;
    height: 310px;
    overflow: hidden;
    box-shadow: 0 10px 24px rgba(0,0,0,0.18);
  }
  .card--back { left: 40px; }
  .card--front { left: 620px; background: var(--white); }

  /* back side */
  .card__photo {
    position: absolute; inset: 0;
    background:
      radial-gradient(ellipse 120px 95px at 62% 58%, var(--cup) 0 60%, rgba(238,240,242,0.6) 75%, transparent 100%),
      radial-gradient(ellipse 170px 120px at 68% 66%, #d9dde0 0 55%, transparent 70%),
      linear-gradient(160deg, var(--wood-light), var(--wood-dark));
  }
  .card__title {
    position: absolute; left: 30px; top: 26px;
    color: var(--white); font-weight: 700; font-size: 24px; letter-spacing: 1px;
  }
  .card__address {
    position: absolute; left: 32px; top: 68px;
    color: var(--white); font-weight: 300; font-size: 18px;
  }
  .card__pin { position: absolute; left: 40px; top: 110px; width: 24px; height: 34px; }

  /* front side */
  .brand {
    position: absolute; left: 0; right: 0; top: 22px;
    text-align: center;
  }
  .brand__mark {
    color: var(--orange); font-weight: 700; font-size: 110px; line-height: 1;
  }
  .brand__name {
    color: var(--ink); font-weight: 400; font-size: 50px; letter-spacing: 2px; line-height: 1.1;
  }

  /* shared contact band */
  .contact-band {
    position: absolute; left: 0; right: 0; bottom: 0; height: 58px;
    background: var(--orange);
    display: flex; align-items: center; justify-content: space-around;
    padding: 0 14px;
  }
  .contact {
    display: flex; align-items: center; gap: 7px;
    color: var(--ink); font-weight: 600; font-size: 14px;
  }
  .contact--web .contact__dot { border-radius: 3px; background: var(--graphite); }
  .contact__dot {
    width: 22px; height: 22px; border-radius: 50%; background: var(--graphite);
  }
</style>
</head>
<body>

<section class="card card--back" aria-label="Business card, back side">
  <div class="card__photo" role="img" aria-label="Photo of a cappuccino with a bicycle drawn in cocoa on the foam, on a rustic wooden table"></div>
  <h2 class="card__title">COFFEE HOUSE</h2>
  <p class="card__address">Street Address</p>
  <svg class="card__pin" viewBox="0 0 24 34" aria-hidden="true">
    <path d="M12 0C5.4 0 0 5.2 0 11.7 0 20 12 34 12 34s12-14 12-22.3C24 5.2 18.6 0 12 0z" fill="#ffffff"/>
    <circle cx="12" cy="11.5" r="4.5" fill="#9a7045"/>
  </svg>
  <div class="contact-band">
    <span class="contact contact--web"><span class="contact__dot"></span>rmcoffeehouse.com</span>
    <span class="contact"><span class="contact__dot"></span>rmcoffeehouse</span>
    <span class="contact"><span class="contact__dot"></span>rmcoffeehouse</span>
  </div>
</section>

<section class="card card--front" aria-label="Business card, front side">
  <div class="brand">
    <div class="brand__mark">RM</div>
    <div class="brand__name">COFFEE HOUSE</div>
  </div>
  <div class="contact-band">
    <span class="contact contact--web"><span class="contact__dot"></span>rmcoffeehouse.com</span>
    <span class="contact"><span class="contact__dot"></span>rmcoffeehouse</span>
    <span class="contact"><span class="contact__dot"></span>rmcoffeehouse</span>
  </div>
</section>

</body>
</html>
```